Need a website for our company

We need a website for our company to showcase all our work for customers to see.
We do all phases of home improvement:
Dormers/Extensions
Basement Remodel
Masonry/Concrete/Pavers/Asphalt
Cultured Stone Veneer
Kitchens
Bathrooms
Pool designs
Outdoor Bathroom
Outdoor Kitchens
Tile work
For reference, something similar to this website: https://brightlanebuilders.example/
Target Market(s)
We are trying to target homeowners.
Coding
Coded - Design and coding required
Number of Pages Required
5+ page
Look and feel

```html
<!DOCTYPE html>
<html lang="en">
<head>
<meta charset="utf-8">
<title>Halvern &amp; Sons Construction Inc</title>
<link href="https://fonts.googleapis.com/css2?family=Inter:wght@300;400;500;600;700&display=swap" rel="stylesheet">
<style>
:root{
  --gold:#d1ac4c;
  --dark:#4a4646;
  --ink:#1d1d1d;
  --text:#3a3a3a;
  --muted:#9a9a9a;
  --light:#f2f2f2;
  --white:#ffffff;
  --line:#d9d9d9;
}
*{margin:0;padding:0;box-sizing:border-box}
html,body{width:1200px;height:3782px;overflow:hidden}
body{position:relative;font-family:"Inter",sans-serif;color:var(--text);background:var(--white)}
.abs{position:absolute}
.topbar{left:0;top:0;width:1200px;height:40px;background:var(--dark);color:var(--white);font-size:13px;display:flex;justify-content:flex-end;align-items:center;padding-right:128px;gap:10px}
.topbar .sep{width:1px;height:18px;background:#bdbdbd}
.topbar .phone{font-size:17px}
.nav{left:0;top:40px;width:1200px;height:58px;background:var(--white)}
.nav ul{list-style:none;display:flex;gap:31px;position:absolute;right:246px;top:20px;font-size:13px;font-weight:500;color:var(--ink)}
.nav li.active{border-bottom:2px solid var(--gold);padding:0 7px 6px}
.logo-box{left:91px;top:0;width:222px;height:125px;background:var(--white);box-shadow:0 2px 8px rgba(0,0,0,.12);z-index:3;display:flex;flex-direction:column;align-items:center;justify-content:center;gap:10px}
.logo-mark{width:34px;height:34px;background:var(--dark)}
.logo-name{font-size:10px;font-weight:600;color:var(--dark);letter-spacing:.5px;text-align:center}
.hero-title{left:0;top:236px;width:1200px;text-align:center;color:var(--white);font-size:53px;font-weight:400;line-height:56px}
.btn-gold{background:var(--gold);color:var(--white);display:flex;align-items:center;justify-content:center;gap:10px}
.hero-btn{left:407px;top:382px;width:160px;height:44px;font-size:19px}
.hero-call{left:591px;top:379px;color:var(--white);display:flex;align-items:center;gap:8px}
.hero-call small{display:block;font-size:16px}
.hero-call strong{display:block;font-size:20px;font-weight:400}
.about-img{left:134px;top:651px;width:409px;height:410px}
h2.about{left:614px;top:694px;font-size:30px;font-weight:700;color:var(--ink)}
.uline{height:4px;background:var(--gold)}
.about p{left:614px;top:765px;width:462px;font-size:16px;line-height:26.6px}
.about-btn{left:611px;top:986px;width:162px;height:45px;font-size:19px}
.section-title{left:0;width:1200px;text-align:center;font-size:30px;font-weight:700;color:var(--ink)}
.service{width:169px;text-align:center;font-size:14px;font-weight:600;color:var(--ink);line-height:16px}
.service .ph{width:169px;height:94px;margin-bottom:12px}
.card{width:309px;height:257px;border:1.5px solid #e6cf8f;border-radius:14px;background:var(--white);padding:36px 38px}
.card .head{display:flex;gap:16px;align-items:flex-start}
.avatar{width:52px;height:52px;border-radius:50%;background:linear-gradient(135deg,#c9c9c9,#8a8a8a);flex:none}
.card .name{font-size:13px;font-weight:700;color:#1e2a50}
.card .role{font-size:11px;color:var(--text);margin:3px 0 2px}
.card .stars{color:#f2b600;font-size:12px;letter-spacing:2px}
.card p{margin-top:30px;font-size:12.5px;line-height:16px;color:#111}
.work .ph{width:234px;height:215px}
.work-label{font-size:20px;font-weight:500;color:var(--white)}
.more-btn{left:504px;top:2676px;width:192px;height:44px;background:var(--white);color:var(--ink);font-size:19px;display:flex;align-items:center;justify-content:center;gap:10px}
.contact-title{left:123px;top:2876px;font-size:29px;font-weight:700;color:var(--ink)}
.field-label{left:135px;font-size:12px;color:#222}
.field{left:135px;width:388px;height:39px;border:1px solid var(--line);border-radius:4px;font-size:11px;color:#bbb;padding:11px 12px}
.send{left:135px;top:3317px;width:107px;height:44px;font-size:19px}
.map{left:583px;top:2879px;width:492px;height:519px;background:linear-gradient(135deg,#eee6d8,#e8e1d3 40%,#f1e3c2);}
.footer-logo{left:132px;top:3548px;width:154px;display:flex;flex-direction:column;align-items:center;gap:10px}
.footer-logo .logo-mark{background:var(--white)}
.footer-logo .logo-name{color:var(--white);font-size:9px}
.f-contact{left:348px;color:var(--white);font-size:13px;display:flex;align-items:center;gap:10px}
.f-title{font-size:14px;font-weight:500;color:var(--white);letter-spacing:.5px}
.f-link{left:693px;color:var(--white);font-size:12.5px}
.social{top:3580px;width:18px;height:18px;border-radius:50%;background:var(--white)}
.copy{left:0;top:3748px;width:1200px;text-align:center;font-size:10.5px;color:var(--white)}
</style>
</head>
<body>

<div class="abs topbar">
  <svg width="14" height="11" viewBox="0 0 14 11" fill="none" stroke="#fff" stroke-width="1.3"><rect x="1" y="1" width="12" height="9"/><path d="M1 1l6 5 6-5"/></svg>
  <span>info@yourcompanyname</span><span class="sep"></span><span>Have any questions?</span><span class="phone">(555) 214-7730</span>
</div>
<header class="abs nav">
  <ul><li class="active">HOME</li><li>ABOUT US</li><li>OUR SERVICES</li><li>OUR WORK</li><li>CONTACT US</li></ul>
</header>
<div class="abs logo-box"><div class="logo-mark"></div><div class="logo-name">HALVERN &amp; SONS CONSTRUCTION INC</div></div>

<svg class="abs" style="left:0;top:98px" width="1200" height="527" role="img" aria-label="Bright modern kitchen with white tiles, oven and window, darkened behind the headline">
  <defs><linearGradient id="heroFill" x1="0" y1="0" x2="1" y2="0"><stop offset="0" stop-color="#5a5754"/><stop offset=".55" stop-color="#6d6b68"/><stop offset="1" stop-color="#8c8d8a"/></linearGradient></defs>
  <polygon points="0,0 1200,0 1200,478 600,527 0,478" fill="url(#heroFill)"/>
</svg>
<h1 class="abs hero-title">Let Us Tackle Your Home<br>Improvement</h1>
<div class="abs btn-gold hero-btn">our work
  <svg width="16" height="14" viewBox="0 0 16 14" fill="none" stroke="#fff" stroke-width="1.6"><path d="M1 7h13M8 1l6 6-6 6"/></svg></div>
<div class="abs hero-call">
  <svg width="42" height="42" viewBox="0 0 42 42" fill="none" stroke="#fff" stroke-width="2"><circle cx="21" cy="21" r="19"/><path d="M14 12l4 0 2 5-3 2c1 3 4 6 7 7l2-3 5 2v4c-9 1-18-8-17-17z"/></svg>
  <div><small>Call us today</small><strong>(555) 300-0000</strong></div>
</div>

<div class="abs about-img" role="img" aria-label="Smiling builder in a hard hat and tool belt giving a thumbs up in front of a house outline" style="background:linear-gradient(160deg,#e9e9e9,#b8b8b8)"></div>
<h2 class="abs about">About Us</h2>
<div class="abs uline" style="left:614px;top:742px;width:85px"></div>
<div class="about"><p class="abs">Lorem ipsum dolor sit amet consectetur. Nunc nam sed neque elit leo. Posuere ut enim suspendisse arcu amet eleifend mi consectetur. Hac in duis purus ac adipiscing id. Sagittis at tempus sollicitudin tincidunt. Urna nullam odio purus duis eu massa ligula. Pulvinar vel ac viverra at sit neque commodo. Nulla enim vitae augue hac bibendum ullamcorper. Nunc ullamcorper massa dolor amet blandit.</p></div>
<div class="abs btn-gold about-btn">Read More
  <svg width="16" height="14" viewBox="0 0 16 14" fill="none" stroke="#fff" stroke-width="1.6"><path d="M1 7h13M8 1l6 6-6 6"/></svg></div>

<svg class="abs" style="left:0;top:1131px" width="1200" height="555"><polygon points="0,0 1200,62 1200,555 0,555" fill="#f2f2f2"/></svg>
<h2 class="abs section-title" style="top:1198px">OUR SERVICES</h2>
<div class="abs uline" style="left:558px;top:1246px;width:84px"></div>

<div class="abs service" style="left:138px;top:1293px"><div class="ph" role="img" aria-label="Brick house with new dormer extension" style="background:linear-gradient(#9fb8d6,#8a5b4a)"></div>Dormers/Extensions</div>
<div class="abs service" style="left:326px;top:1293px"><div class="ph" role="img" aria-label="Remodeled basement with stairs" style="background:linear-gradient(#d7d7d7,#8d8a85)"></div>Basement Remodel</div>
<div class="abs service" style="left:514px;top:1293px"><div class="ph" role="img" aria-label="Paved asphalt driveway" style="background:linear-gradient(#9aa38e,#6b6b6b)"></div>Masonry/Concrete/<br>Pavers/Asphalt</div>
<div class="abs service" style="left:702px;top:1293px"><div class="ph" role="img" aria-label="House entrance with cultured stone veneer" style="background:linear-gradient(#8d8a80,#5c5650)"></div>Cultured Stone<br>Veneer</div>
<div class="abs service" style="left:892px;top:1293px"><div class="ph" role="img" aria-label="Bright kitchen with island" style="background:linear-gradient(#e8e8e6,#a9a6a0)"></div>Kitchens</div>

<div class="abs service" style="left:138px;top:1460px"><div class="ph" role="img" aria-label="White modern bathroom" style="background:linear-gradient(#e6e6e6,#9b9b9b)"></div>Bathrooms</div>
<div class="abs service" style="left:326px;top:1460px"><div class="ph" role="img" aria-label="Backyard swimming pool with lawn" style="background:linear-gradient(#6e9a4f,#5ab6d9)"></div>Pool designs</div>
<div class="abs service" style="left:514px;top:1460px"><div class="ph" role="img" aria-label="Outdoor bathroom with freestanding tub" style="background:linear-gradient(#6a4a32,#8b9a6a)"></div>Outdoor Bathroom</div>
<div class="abs service" style="left:702px;top:1460px"><div class="ph" role="img" aria-label="Covered outdoor kitchen with stone fireplace" style="background:linear-gradient(#8a6a4a,#5e4634)"></div>Outdoor Kitchens</div>
<div class="abs service" style="left:892px;top:1460px"><div class="ph" role="img" aria-label="Patterned wall and floor tile work" style="background:linear-gradient(#d2d0cb,#9c9a94)"></div>Tile work</div>

<h2 class="abs section-title" style="top:1756px">TESTIMONIALS</h2>
<div class="abs uline" style="left:558px;top:1803px;width:84px"></div>
<svg class="abs" style="left:84px;top:1947px" width="20" height="20" viewBox="0 0 20 20" fill="none" stroke="#222" stroke-width="1.6"><path d="M18 10H3M9 4l-6 6 6 6"/></svg>
<svg class="abs" style="left:1112px;top:1951px" width="20" height="20" viewBox="0 0 20 20" fill="none" stroke="#222" stroke-width="1.6"><path d="M2 10h15M11 4l6 6-6 6"/></svg>

<div class="abs card" style="left:123px;top:1844px;border-bottom:4px solid #111">
  <div class="head"><div class="avatar" role="img" aria-label="Customer portrait"></div><div><div class="name">Dana Whitfield</div><div class="role">Family Owner</div><div class="stars">★★★★★</div></div></div>
  <p>Lorem ipsum dolor sit amet, consectetur adipiscing elit, sed do eiusmod tempor incididunt ut labore et dolore magna aliqua.</p>
</div>
<div class="abs card" style="left:452px;top:1844px">
  <div class="head"><div class="avatar" role="img" aria-label="Customer portrait" style="background:linear-gradient(135deg,#e0a080,#a04030)"></div><div><div class="name">Dana Whitfield</div><div class="role">Family Owner</div><div class="stars">★★★★★</div></div></div>
  <p>Lorem ipsum dolor sit amet, consectetur adipiscing elit, sed do eiusmod tempor incididunt ut labore et dolore magna aliqua.</p>
</div>
<div class="abs card" style="left:781px;top:1839px;box-shadow:0 4px 10px rgba(0,0,0,.06)">
  <div class="head"><div class="avatar" role="img" aria-label="Customer portrait" style="background:linear-gradient(135deg,#6a6a6a,#2a2a2a)"></div><div><div class="name">Dana Whitfield</div><div class="role">Family Owner</div><div class="stars">★★★★★</div></div></div>
  <p>Lorem ipsum dolor sit amet, consectetur adipiscing elit, sed do eiusmod tempor incididunt ut labore et dolore magna aliqua.</p>
</div>

<svg class="abs" style="left:0;top:2174px" width="1200" height="657"><polygon points="0,66 1200,0 1200,602 0,657" fill="#d1ac4c"/></svg>
<h2 class="abs section-title" style="top:2268px;color:var(--white)">OUR RECENT WORK</h2>
<div class="abs" style="left:573px;top:2316px;width:84px;height:4px;background:var(--white)"></div>
<div class="abs work" style="left:119px;top:2372px"><div class="ph" role="img" aria-label="Marble bathroom with copper bathtub" style="background:linear-gradient(135deg,#d9d3ca,#8a5a3a)"></div></div>
<div class="abs work" style="left:361px;top:2372px"><div class="ph" role="img" aria-label="Turquoise swimming pool with stone deck" style="background:linear-gradient(135deg,#1aa6d6,#7fd5ee)"></div></div>
<div class="abs work" style="left:605px;top:2372px"><div class="ph" role="img" aria-label="Remodeled basement kitchen with wood floor" style="background:linear-gradient(#ededed,#9b968d)"></div></div>
<div class="abs work" style="left:845px;top:2372px"><div class="ph" role="img" aria-label="Outdoor kitchen with stone fireplace and grill" style="background:linear-gradient(#6f8a4c,#7a6a5c)"></div></div>
<div class="abs work-label" style="left:124px;top:2600px">Bathrooms</div>
<div class="abs work-label" style="left:366px;top:2600px">Pool Design</div>
<div class="abs work-label" style="left:604px;top:2603px">Basement Remodel</div>
<div class="abs work-label" style="left:851px;top:2600px">Kitchen</div>
<div class="abs more-btn">More our work
  <svg width="16" height="14" viewBox="0 0 16 14" fill="none" stroke="#222" stroke-width="1.6"><path d="M1 7h13M8 1l6 6-6 6"/></svg></div>

<h2 class="abs contact-title">GET IN CONTACT WITH US!</h2>
<div class="abs uline" style="left:123px;top:2946px;width:83px"></div>
<div class="abs field-label" style="top:2975px">Your name</div>
<div class="abs field" style="top:2992px">Your name</div>
<div class="abs field-label" style="top:3049px">Phone number</div>
<div class="abs field" style="top:3067px">Phone number</div>
<div class="abs field-label" style="top:3124px">Email</div>
<div class="abs field" style="top:3141px">Email</div>
<div class="abs field-label" style="top:3198px">Message</div>
<div class="abs field" style="top:3221px;width:392px;height:89px"></div>
<div class="abs btn-gold send">SEND</div>
<div class="abs map" role="img" aria-label="Street map showing the company location"></div>

<svg class="abs" style="left:0;top:3442px" width="1200" height="340"><polygon points="0,42 600,0 1200,42 1200,340 0,340" fill="#494545"/></svg>
<div class="abs footer-logo"><div class="logo-mark"></div><div class="logo-name">HALVERN &amp; SONS CONSTRUCTION INC</div></div>
<div class="abs f-contact" style="top:3559px"><svg width="16" height="16" viewBox="0 0 16 16" fill="none" stroke="#d1ac4c" stroke-width="1.4"><path d="M8 15s5-5 5-9A5 5 0 0 0 3 6c0 4 5 9 5 9z"/><circle cx="8" cy="6" r="2"/></svg>Your location here</div>
<div class="abs f-contact" style="top:3588px"><svg width="16" height="13" viewBox="0 0 16 13" fill="none" stroke="#d1ac4c" stroke-width="1.4"><rect x="1" y="1" width="14" height="11"/><path d="M1 1l7 6 7-6"/></svg>info@halvernandsons.example</div>
<div class="abs f-contact" style="top:3618px"><svg width="16" height="16" viewBox="0 0 16 16" fill="none" stroke="#d1ac4c" stroke-width="1.4"><path d="M3 1h3l1.5 4-2 1.5c1 2 2.5 3.5 4.5 4.5L11.5 9l4 1.5v3C8 15 1 8 3 1z"/></svg>000 555 998</div>
<div class="abs f-title" style="left:693px;top:3543px">QUICKLINKS</div>
<div class="abs f-link" style="top:3572px">Home</div>
<div class="abs f-link" style="top:3598px">About Us</div>
<div class="abs f-link" style="top:3625px">Our Services</div>
<div class="abs f-link" style="top:3652px">Our Work</div>
<div class="abs f-link" style="top:3678px">Contact Us</div>
<div class="abs f-title" style="left:880px;top:3543px">CONNECTED WITH US</div>
<div class="abs social" style="left:884px"></div>
<div class="abs social" style="left:919px"></div>
<div class="abs social" style="left:953px"></div>
<div class="abs social" style="left:988px"></div>
<div class="abs social" style="left:1021px"></div>
<div class="abs" style="left:38px;top:3714px;width:1075px;height:1px;background:#8a8686"></div>
<div class="abs copy">©2023 Halvernandsons. All rights reserved.</div>

</body>
</html>
```